its a new company based in Christchurch new Zealand building computers ,repairs, upgrades and anything computers for the general public,i like bright happy colours like yellows, greens reds anything that stands out and it needs to communicant trust and security towards my new company,i have no logo yet,

Target Market(s)

target market of all ages

Industry/Entity Type

Building

Contact Information for Business Card

Pixel Harbour Limited,ph-0214862735,email-bluefoxtrail17@mailnest.example,4c marlowe rd,fernvale

```html
<!DOCTYPE html>
<html lang="en">
<head>
<meta charset="utf-8">
<title>Pixel Harbour Limited — Business Card</title>
<link rel="stylesheet" href="https://fonts.googleapis.com/css2?family=Audiowide&family=Open+Sans:wght@400&display=swap">
<style>
  :root {
    --page-bg: #ffffff;
    --card-black: #050608;
    --card-deep: #0a1824;
    --glow-blue: #0e3b5c;
    --gold: #f2b41a;
    --gold-light: #ffd54a;
    --contact-blue: #2a9fd8;
    --band-black: #06080a;
  }
  * { margin: 0; padding: 0; box-sizing: border-box; }
  html, body {
    width: 1200px;
    height: 900px;
    overflow: hidden;
    background: var(--page-bg);
  }
  .canvas {
    position: relative;
    width: 1200px;
    height: 900px;
  }
  .business-card {
    position: absolute;
    left: 110px;
    top: 160px;
    width: 980px;
    height: 580px;
    border-radius: 42px;
    overflow: hidden;
    background:
      radial-gradient(ellipse 60% 45% at 55% 38%, var(--glow-blue) 0%, rgba(14,59,92,0) 100%),
      linear-gradient(180deg, var(--card-deep) 0%, var(--card-black) 70%);
  }
  .brand-artwork {
    position: absolute;
    left: 40px;
    top: 30px;
    width: 240px;
    height: 300px;
    border-radius: 10px;
    background: linear-gradient(160deg, #e0a21c 0%, #6b4a10 22%, #1b2a3a 45%, #2a6fae 70%, #0c1018 100%);
  }
  .company-name {
    position: absolute;
    left: 295px;
    top: 95px;
    font-family: "Audiowide", sans-serif;
    font-weight: 400;
    font-size: 64px;
    line-height: 78px;
    color: var(--gold);
    letter-spacing: 1px;
  }
  .contact-band {
    position: absolute;
    left: 0;
    right: 0;
    top: 360px;
    height: 180px;
    background: var(--band-black);
    border-top: 4px solid var(--gold);
    border-bottom: 4px solid var(--gold);
  }
  .contact-list {
    list-style: none;
    position: absolute;
    left: 70px;
    top: 26px;
  }
  .contact-item {
    display: flex;
    align-items: center;
    gap: 14px;
    height: 40px;
    font-family: "Open Sans", sans-serif;
    font-size: 27px;
    color: var(--contact-blue);
  }
  .contact-icon {
    width: 30px;
    height: 30px;
    flex: none;
  }
</style>
</head>
<body>
<main class="canvas">
  <section class="business-card">
    <div class="brand-artwork" role="img" aria-label="Illustration of a gold crown on a black computer tower with a monitor"></div>
    <h1 class="company-name">Pixel Harbour<br>Limited</h1>

    <div class="contact-band">
      <ul class="contact-list">
        <li class="contact-item">
          <svg class="contact-icon" viewBox="0 0 24 24" aria-hidden="true">
            <path fill="var(--gold)" d="M6.6 10.8a15.1 15.1 0 0 0 6.6 6.6l2.2-2.2a1 1 0 0 1 1-.25 11.4 11.4 0 0 0 3.6.57 1 1 0 0 1 1 1V20a1 1 0 0 1-1 1A17 17 0 0 1 3 4a1 1 0 0 1 1-1h3.5a1 1 0 0 1 1 1c0 1.25.2 2.45.57 3.57a1 1 0 0 1-.25 1z"/>
          </svg>
          <span>0214862735,</span>
        </li>
        <li class="contact-item">
          <svg class="contact-icon" viewBox="0 0 24 24" aria-hidden="true">
            <rect x="2" y="5" width="20" height="14" rx="1.5" fill="var(--gold)"/>
            <path d="M2.5 6 12 13l9.5-7" fill="none" stroke="var(--band-black)" stroke-width="1.6"/>
          </svg>
          <span>bluefoxtrail17@mailnest.example,</span>
        </li>
        <li class="contact-item">
          <svg class="contact-icon" viewBox="0 0 24 24" aria-hidden="true">
            <path fill="var(--gold)" d="M12 3 2 11.5h3V21h5.5v-5.5h3V21H19v-9.5h3z"/>
          </svg>
          <span>4c marlowe rd,fernvale</span>
        </li>
      </ul>
    </div>
  </section>
</main>
</body>
</html>
```